New Dental Office Needs an Attractive and user friendly Website Designed

I need a website for a new dental office. The Name is Maplecrest Dentistry. I would like a Modern design with a user friendly interface and usability.
I would like a landing page, a page that lists the services we offer: Cosmetic Dentistry, Implants, Dental Hygiene, Emergency Services, Restorations, Dentures
Target Market(s)
Mid to upper class
Industry/Entity Type
Dentistry
Coding
Coded - Design and coding required
Number of Pages Required
1 page
Requirements
Must have
- Landing page that has a scheduling option, Procedures, operating hours, and contact us info
Nice to have
- Appealing design, Soft comforting colors. Easy to navigate page, Modern and professional.

```html
<!DOCTYPE html>
<html lang="en">
<head>
<meta charset="utf-8">
<title>Maplecrest Dentistry</title>
<link href="https://fonts.googleapis.com/css2?family=Playfair+Display:wght@400;500&family=Poppins:ital,wght@0,300;0,400;0,500;1,400&display=swap" rel="stylesheet">
<style>
:root{
  --teal:#1e8fa3;
  --teal-dark:#177a8c;
  --ink:#0f3d4a;
  --text:#3d4f56;
  --muted:#5d6d73;
  --pale:#eaf6f9;
  --pale-2:#dff1f5;
  --panel:#62b6c5;
  --line:#d6e8ed;
  --white:#ffffff;
}
*{margin:0;padding:0;box-sizing:border-box}
html,body{width:1200px;height:3138px;overflow:hidden}
body{position:relative;background:var(--white);font-family:'Poppins',sans-serif;color:var(--text)}
.abs{position:absolute}
.serif{font-family:'Playfair Display',serif;font-weight:400;color:var(--ink)}
.label{font-size:11px;letter-spacing:1.6px;text-transform:uppercase;color:var(--muted);display:flex;align-items:center;gap:10px}
.label::before{content:"";width:7px;height:7px;border-radius:50%;background:var(--teal)}
.btn-arrow{width:26px;height:26px;border-radius:4px;background:var(--teal);display:flex;align-items:center;justify-content:center}
.btn-arrow.light{background:var(--white)}
.logo{font-family:'Playfair Display',serif;font-size:22px;font-weight:500;color:var(--ink);white-space:nowrap}

/* hero */
.hero{left:0;top:0;width:1200px;height:587px;background:linear-gradient(180deg,#f6fbfc 0%,#d5eef3 55%,#b9e2ea 100%);clip-path:polygon(0 0,1200px 0,1200px 524px,1137px 587px,61px 587px,0 524px)}
.hero-photo{left:470px;top:55px;width:430px;height:532px;border-radius:220px 220px 0 0;background:radial-gradient(ellipse at 50% 35%,#e9c9b4 0%,#d8b29a 35%,#eef6f8 70%,rgba(238,246,248,0) 100%)}
.nav{top:24px;left:157px;width:886px;height:34px;display:flex;align-items:center}
.nav-links{margin-left:auto;display:flex;gap:31px;font-size:13px;color:var(--ink);align-items:center}
.nav-links .active{color:var(--teal)}
.nav-cta{margin-left:32px;background:var(--teal);color:var(--white);font-size:13px;height:35px;padding:0 5px 0 19px;border-radius:4px;display:flex;align-items:center;gap:20px}
.hero-note{left:157px;top:201px;width:285px;height:80px;background:rgba(255,255,255,.55);border-radius:14px;padding:16px 16px;font-size:11.5px;line-height:17px;color:var(--text)}
.hero-title{left:157px;top:372px;font-size:61px;line-height:64px}
.hero-sub{left:157px;top:516px;font-size:15.5px;font-style:italic;color:var(--ink)}
.phone-pill{left:832px;top:368px;height:32px;background:var(--white);border-radius:16px;padding:0 5px 0 16px;display:flex;align-items:center;gap:12px;font-size:15px;color:var(--teal)}
.phone-pill .dot{width:24px;height:24px;border-radius:50%;background:var(--pale);display:flex;align-items:center;justify-content:center}
.phone-note{left:832px;top:412px;font-size:11.5px;line-height:17px;color:var(--text);width:220px}

/* about */
.about-label{left:157px;top:652px}
.about-lead{left:457px;top:648px;width:590px;font-size:27px;font-weight:300;line-height:37.5px;color:var(--ink)}
.btn-outline{border:1px solid var(--teal);border-radius:4px;background:var(--white);height:35px;display:flex;align-items:center;justify-content:space-between;padding:0 4px 0 18px;font-size:13px;color:var(--teal)}
.about-btn{left:457px;top:856px;width:139px}
.about-rule{left:457px;top:909px;width:586px;height:1px;background:var(--line)}
.about-photo{left:157px;top:928px;width:255px;height:188px;border-radius:16px;background:linear-gradient(135deg,#c9d3d8 0%,#e8ecee 45%,#8fd0dc 100%)}
.feature{top:960px;width:285px}
.feature .ico{width:38px;height:38px;border-radius:50%;background:var(--pale-2);display:flex;align-items:center;justify-content:center}
.feature h3{margin-top:18px;font-size:13px;font-weight:500;color:var(--ink)}
.feature p{margin-top:14px;font-size:11.5px;line-height:17px;color:var(--text)}

/* services */
.services{left:0;top:1178px;width:1200px;height:430px;background:var(--pale)}
.center-label{left:0;width:1200px;justify-content:center}
.services-title{left:0;top:1267px;width:1200px;text-align:center;font-size:28px;line-height:33px}
.svc-card{top:1365px;width:285px;height:181px;background:var(--white);border-radius:10px;padding:20px 18px}
.svc-card.active{border:1px solid #9ccfda}
.svc-card .ico{width:36px;height:36px;border-radius:50%;background:var(--teal);display:flex;align-items:center;justify-content:center}
.svc-card h3{margin-top:17px;font-size:13px;font-weight:500;color:var(--ink)}
.svc-card p{margin-top:13px;font-size:11.5px;line-height:17px;color:var(--text)}
.carousel-arrow{top:1445px}

/* appointment */
.appt-label{left:157px;top:1697px}
.appt-title{left:157px;top:1720px;font-size:28px;line-height:33px}
.appt-text{left:157px;top:1806px;width:365px;font-size:11.5px;line-height:17px}
.hours{left:157px;top:1888px;width:361px;height:150px;border:1px solid var(--line);border-radius:10px;overflow:hidden}
.hours-head{height:55px;background:var(--pale);padding:0 18px;display:flex;align-items:center;font-size:13px;font-weight:500;color:var(--ink)}
.hours-row{margin:0 18px;height:39px;display:flex;align-items:center;justify-content:space-between;font-size:13px;color:var(--ink)}
.hours-row+.hours-row{border-top:1px solid var(--line)}
.hours-row span:last-child{color:var(--teal)}
.hours-row:first-of-type{margin-top:8px}
.form-panel{left:607px;top:1671px;width:436px;height:391px;background:var(--panel);border-radius:14px;clip-path:polygon(64px 0,100% 0,100% 100%,0 100%,0 64px)}
.form-panel h2{position:absolute;top:50px;left:0;width:100%;text-align:center;font-size:19px;font-weight:500;color:var(--white)}
.form-panel .intro{position:absolute;top:88px;left:50px;width:336px;text-align:center;font-size:11px;line-height:17px;color:#eaf8fb}
.field{position:absolute;height:35px;border:1px solid rgba(255,255,255,.55);border-radius:4px;font-size:11px;color:#e6f6f9;display:flex;align-items:center;padding:0 14px}
.field .floating{position:absolute;top:-8px;left:10px;background:var(--panel);padding:0 4px;font-size:10px}
.field.filled{color:var(--white);font-size:12px}
.submit{position:absolute;left:37px;top:306px;width:362px;height:36px;border:1px solid rgba(255,255,255,.8);border-radius:4px;display:flex;align-items:center;justify-content:center;color:var(--white);font-size:13px;font-weight:500}
.submit .btn-arrow{position:absolute;right:4px;top:4px}

/* testimonials */
.testimonials{left:0;top:2125px;width:1200px;height:496px;background:var(--pale)}
.quote{text-align:center;font-size:11.5px;line-height:17px;color:var(--text)}
.quote .name{font-size:13px;font-weight:500;color:var(--ink)}
.quote .stars{margin:7px 0 12px;color:var(--teal);font-size:11px;letter-spacing:3px}
.photo{border-radius:12px}
.t-label{left:607px;top:2189px}
.t-title{left:607px;top:2213px;font-size:28px;line-height:33px}
.t-btn{left:607px;top:2300px;width:204px}

/* contact cta */
.footer-bg{left:0;top:2826px;width:1200px;height:312px;background:var(--pale)}
.cta{left:157px;top:2685px;width:886px;height:265px;border-radius:36px;background:linear-gradient(180deg,#bfeaf2 0%,#8fd3df 60%,#5fb7c6 100%);overflow:hidden}
.cta-shape{position:absolute;border-radius:120px;background:rgba(140,225,238,.75);transform:rotate(-40deg)}
.cta-label{left:207px;top:2737px}
.cta-title{left:207px;top:2760px;font-size:28px;line-height:33px}
.cta-text{left:207px;top:2814px;width:380px;font-size:11.5px;line-height:17px;color:var(--ink)}
.cta-btn{left:207px;top:2866px;width:234px;height:35px;border:none}
.dentist{left:750px;top:2637px;width:260px;height:313px;border-radius:130px 130px 0 0;background:linear-gradient(180deg,#d9b9a3 0%,#e7ece f 40%,#f4f7f8 60%,#cfe3e8 100%)}

/* footer */
.f-logo{left:157px;top:3017px}
.social{top:3015px;height:36px;border:1px solid #b9d9e0;border-radius:4px;display:flex;align-items:center;gap:10px;padding:0 12px 0 8px;font-size:13px;color:var(--ink);background:var(--white)}
.social .sq{width:20px;height:20px;border-radius:3px;background:var(--pale-2)}
.f-rule{left:157px;top:3082px;width:886px;height:1px;background:var(--line)}
.copy{left:157px;top:3102px;font-size:11.5px;color:var(--text)}
.f-links{left:0;top:3100px;width:1043px;display:flex;justify-content:flex-end;font-size:11.5px;color:var(--ink)}
.f-links span{padding:0 31px;border-left:1px solid var(--line)}
.f-links span:first-child{border-left:none}
.f-links span:last-child{padding-right:0}
</style>
</head>
<body>

<!-- HERO -->
<section class="abs hero"></section>
<div class="abs hero-photo" role="img" aria-label="Portrait of a smiling woman with short brown hair"></div>

<header class="abs nav">
  <div class="logo">Maplecrest Dentistry</div>
  <nav class="nav-links">
    <span class="active">Home</span>
    <span>Services &nbsp;<svg width="10" height="7" viewBox="0 0 10 7"><path d="M1 1l4 4 4-4" fill="none" stroke="#0f3d4a" stroke-width="1.5"/></svg></span>
    <span>About</span>
    <span>Contact</span>
  </nav>
  <div class="nav-cta">Schedule an Appointment
    <span class="btn-arrow light"><svg width="12" height="12" viewBox="0 0 12 12"><path d="M2 6h8M7 3l3 3-3 3" fill="none" stroke="#1e8fa3" stroke-width="1.4"/></svg></span>
  </div>
</header>

<p class="abs hero-note">Our experienced team offers a range of services in a friendly atmosphere, ensuring your dental health is our top priority.</p>
<h1 class="abs serif hero-title">Smile Brighter with<br>Confidence</h1>
<p class="abs hero-sub">Compassionate, Modern Dental Care in a Calming Environment.</p>
<div class="abs phone-pill">+49 0176 552418
  <span class="dot"><svg width="10" height="10" viewBox="0 0 10 10"><path d="M2 8l6-6M3 2h5v5" fill="none" stroke="#1e8fa3" stroke-width="1.3"/></svg></span>
</div>
<p class="abs phone-note">We're here to answer your questions and help you schedule your visit.</p>

<!-- ABOUT -->
<div class="abs label about-label">About Us</div>
<p class="abs about-lead">We're committed to providing expert dental care in a modern, relaxing space. From preventive hygiene to advanced implants and cosmetic treatments, we're here to keep your smile healthy and bright.</p>
<div class="abs btn-outline about-btn">Learn More
  <span class="btn-arrow"><svg width="12" height="12" viewBox="0 0 12 12"><path d="M2 6h8M7 3l3 3-3 3" fill="none" stroke="#fff" stroke-width="1.4"/></svg></span>
</div>
<div class="abs about-rule"></div>
<div class="abs about-photo" role="img" aria-label="Dentist examining a smiling patient in the treatment chair"></div>

<div class="abs feature" style="left:457px">
  <div class="ico"><svg width="18" height="18" viewBox="0 0 18 18"><path d="M4 9l3.5 3.5L14 6" fill="none" stroke="#1e8fa3" stroke-width="1.6"/></svg></div>
  <h3>Comfort-Focused Care</h3>
  <p>From cozy blankets to gentle techniques, your comfort is our priority. We make every visit feel calm, relaxing, and stress-free.</p>
</div>
<div class="abs feature" style="left:756px">
  <div class="ico"><svg width="18" height="18" viewBox="0 0 18 18"><rect x="4" y="3" width="10" height="12" rx="1.5" fill="none" stroke="#1e8fa3" stroke-width="1.4"/><path d="M6.5 7h5M6.5 10h5" stroke="#1e8fa3" stroke-width="1.4"/></svg></div>
  <h3>Comprehensive Dental Services</h3>
  <p>From cleanings to cosmetic treatments and implants, we offer complete dental care for the whole family — all under one roof.</p>
</div>

<!-- SERVICES -->
<section class="abs services"></section>
<div class="abs label center-label" style="top:1242px">Services</div>
<h2 class="abs serif services-title">Creating Beautiful Smiles Through<br>Transformative Dentistry</h2>

<svg class="abs carousel-arrow" style="left:122px" width="22" height="22" viewBox="0 0 22 22"><path d="M19 11H3M9 5l-6 6 6 6" fill="none" stroke="#0f3d4a" stroke-width="1.4"/></svg>
<svg class="abs carousel-arrow" style="left:1057px" width="22" height="22" viewBox="0 0 22 22"><path d="M3 11h16M13 5l6 6-6 6" fill="none" stroke="#1e8fa3" stroke-width="1.4"/></svg>

<div class="abs svc-card active" style="left:157px">
  <div class="ico"><svg width="16" height="16" viewBox="0 0 16 16"><path d="M8 2l1.5 4.5L14 8l-4.5 1.5L8 14l-1.5-4.5L2 8l4.5-1.5z" fill="#fff"/></svg></div>
  <h3>Cosmetic Dentistry</h3>
  <p>Brighten your smile with treatments like teeth whitening, veneers, and bonding designed to enhance the appearance of your teeth.</p>
</div>
<div class="abs svc-card" style="left:458px">
  <div class="ico"><svg width="16" height="16" viewBox="0 0 16 16"><path d="M8 2v12M4 5h8M5 9h6" stroke="#fff" stroke-width="1.5"/></svg></div>
  <h3>Implants</h3>
  <p>Restore missing teeth with natural-looking dental implants — a long-lasting solution for comfort, function, and confidence.</p>
</div>
<div class="abs svc-card" style="left:758px">
  <div class="ico"><svg width="16" height="16" viewBox="0 0 16 16"><path d="M3 8l3.5 3.5L13 5" fill="none" stroke="#fff" stroke-width="1.6"/></svg></div>
  <h3>Dental Hygiene</h3>
  <p>Keep your teeth and gums healthy with regular cleanings, exams, and personalized preventive care from our hygiene team.</p>
</div>

<!-- APPOINTMENT -->
<div class="abs label appt-label">Appointment</div>
<h2 class="abs serif appt-title" style="top:1720px">Effortless Online Booking for<br>Your Dental Visit</h2>
<p class="abs appt-text">At Maplecrest Dentistry, we understand your time is valuable. That's why we offer a streamlined online booking system that allows you to schedule your appointment at your convenience.</p>
<div class="abs hours">
  <div class="hours-head">Opening Hours</div>
  <div class="hours-row"><span>Monday–Friday:</span><span>8:00 AM – 5:00 PM</span></div>
  <div class="hours-row"><span>Saturday–Sunday:</span><span>Closed</span></div>
</div>

<div class="abs form-panel">
  <h2>Ready to Book Your Appointment?</h2>
  <p class="intro">Our team is here to help. Fill out the form below, and we'll reach out to guide you through the process.</p>
  <div class="field filled" style="left:37px;top:156px;width:362px"><span class="floating">Full Name*</span>John Doe</div>
  <div class="field" style="left:37px;top:206px;width:173px">Phone*</div>
  <div class="field" style="left:225px;top:206px;width:174px">Email*</div>
  <div class="field" style="left:37px;top:256px;width:362px;justify-content:space-between">Select Date
    <svg width="12" height="12" viewBox="0 0 12 12"><rect x="1.5" y="2.5" width="9" height="8" rx="1" fill="none" stroke="#fff" stroke-width="1"/><path d="M1.5 5h9M4 1v2.5M8 1v2.5" stroke="#fff" stroke-width="1"/></svg>
  </div>
  <div class="submit">Submit Now
    <span class="btn-arrow light"><svg width="12" height="12" viewBox="0 0 12 12"><path d="M2 6h8M7 3l3 3-3 3" fill="none" stroke="#1e8fa3" stroke-width="1.4"/></svg></span>
  </div>
</div>

<!-- TESTIMONIALS -->
<section class="abs testimonials"></section>

<div class="abs quote" style="left:157px;top:2222px;width:156px">
  <div class="name">Lena R.</div>
  <div class="stars">★★★★★</div>
  <p>The best dental care I have ever experienced! Professional and friendly staff made me feel like family... would highly recommend to anyone!!!</p>
</div>
<div class="abs photo" style="left:157px;top:2402px;width:156px;height:157px;background:linear-gradient(160deg,#5fd6d8 0%,#7fe0df 50%,#f2c64a 100%)" role="img" aria-label="Smiling woman in a yellow top framing her face with her hands"></div>

<div class="abs photo" style="left:352px;top:2188px;width:216px;height:212px;background:linear-gradient(160deg,#4e7d8c 0%,#8aa7ad 45%,#c9a58a 100%)" role="img" aria-label="Young man with curly hair smiling outdoors"></div>
<div class="abs quote" style="left:352px;top:2426px;width:216px">
  <div class="name">Marcus T.</div>
  <div class="stars">★★★★★</div>
  <p>This is a great place to go take care of your teeth. The team was very professional examining and providing with solutions by priority.</p>
</div>

<div class="abs label t-label">Testimonials</div>
<h2 class="abs serif t-title">Why People Choose<br>Our Dental Practice?</h2>
<div class="abs btn-outline t-btn">Read All Testimonials
  <span class="btn-arrow"><svg width="12" height="12" viewBox="0 0 12 12"><path d="M2 6h8M7 3l3 3-3 3" fill="none" stroke="#fff" stroke-width="1.4"/></svg></span>
</div>
<div class="abs photo" style="left:607px;top:2365px;width:237px;height:156px;background:linear-gradient(135deg,#7a3b2c 0%,#c27a5a 40%,#f1dcc0 75%,#d9a06f 100%)" role="img" aria-label="Smiling woman standing under autumn trees"></div>

<div class="abs photo" style="left:888px;top:2188px;width:156px;height:157px;background:linear-gradient(160deg,#c7d8e6 0%,#b99577 45%,#4f7aa8 100%)" role="img" aria-label="Smiling woman in a sun hat giving a thumbs up"></div>
<div class="abs quote" style="left:888px;top:2371px;width:156px">
  <div class="name">Nora P.</div>
  <div class="stars">★★★★★</div>
  <p>This is a wonderful dental office with very professional and friendly staff and up to date technology. They were so nice.</p>
</div>

<!-- CONTACT CTA -->
<div class="abs footer-bg"></div>
<div class="abs cta">
  <div class="cta-shape" style="left:560px;top:80px;width:320px;height:110px"></div>
  <div class="cta-shape" style="left:700px;top:20px;width:260px;height:90px"></div>
</div>
<div class="abs dentist" style="background:linear-gradient(180deg,#d9b9a3 0%,#eef2f3 38%,#f7f9fa 65%,#cfe3e8 100%)" role="img" aria-label="Smiling dentist in a white coat holding a dental mirror"></div>
<div class="abs label cta-label">Contact</div>
<h2 class="abs serif cta-title">Let's Take Care of Your Smile</h2>
<p class="abs cta-text">Whether it's your first visit or your next check-up, we're here to make it easy, comfortable, and stress-free.</p>
<div class="abs btn-outline cta-btn">Schedule an Appointment
  <span class="btn-arrow"><svg width="12" height="12" viewBox="0 0 12 12"><path d="M2 6h8M7 3l3 3-3 3" fill="none" stroke="#fff" stroke-width="1.4"/></svg></span>
</div>

<!-- FOOTER -->
<div class="abs logo f-logo">Maplecrest Dentistry</div>
<div class="abs social" style="left:772px"><span class="sq"></span>Community
  <svg width="10" height="10" viewBox="0 0 10 10"><path d="M2 8l6-6M3 2h5v5" fill="none" stroke="#0f3d4a" stroke-width="1.3"/></svg>
</div>
<div class="abs social" style="left:917px"><span class="sq"></span>Network
  <svg width="10" height="10" viewBox="0 0 10 10"><path d="M2 8l6-6M3 2h5v5" fill="none" stroke="#0f3d4a" stroke-width="1.3"/></svg>
</div>
<div class="abs f-rule"></div>
<p class="abs copy">Copyright ©2025 Maplecrest Dentistry, all rights reserved.</p>
<div class="abs f-links"><span>Home</span><span>Services</span><span>About</span><span>Contact</span></div>

</body>
</html>
```